LORM Business Card Design Project

Company Name: LORM (Bright Harbor Computing Solutions) PGH.
Office Address: Office No 718, Saffron Crest Tower, Palmwood Garden Heights, Dubai, U.A.E
Company line of business:
1) Currently we have a POS solution for retail outlets like duty free shops, supermarkets, department stores etc... The solution is deployed in Coastline Travel Retail on 350 POS and in Sandgate Airport Retail on 100 POS. So our main line of business is the deployment of this solution in retail outlets locally or regionally. We have already deployed the solution in India and Australia.
2) Integration of other third party POS systems with an online credit authorization netwotk in the UAE. This will enable POS applications to connect directly to the acquiring banks without needing an EFT terminal like Paxtrel or Movarski. The credit card payment is completed at the POS.
3) Other solutions that are targeting retail outlets like mobile POS, queue busting solutions, stock taking solutions using hand held devices, transaction capture systems, etc...
4) Other IT services like support of call center solutions from Northwind Callworks and development of new solutions as per customer requirements.
We need a business card design for the company. We don't have any specific requirements and will eave up to the designers to come up with creative designs. At the moment we still don't have a letter head design and the only thing that we have is the company logo that we will upload shortly.
Updates
Dear All,
I just uploaded the logo source files. I am sorry for the delay.
Regards
Samir Odwani
I would like the business cards to have the following details:
Company Tel No
Company Fax No
Company Website Address
Employee Name
Employee Title
Employee Mobile Number
Employee Email Address

```html
<!DOCTYPE html>
<html lang="en">
<head>
<meta charset="utf-8">
<title>LORM Business Card</title>
<link rel="stylesheet" href="https://fonts.googleapis.com/css2?family=Questrial&family=Open+Sans:wght@400&display=swap">
<style>
  :root {
    --page-bg: #ffffff;
    --card-light: #fbfbfb;
    --card-shade: #e2e3e5;
    --brand-blue: #1679a8;
    --brand-blue-deep: #0d5e88;
    --brand-blue-light: #2a93c2;
    --rule-grey: #a9abad;
    --name-blue: #1b7fb0;
    --title-ink: #1e1e1e;
    --body-ink: #5a5a5a;
  }
  * { margin: 0; padding: 0; box-sizing: border-box; }
  html, body {
    width: 1200px;
    height: 800px;
    overflow: hidden;
    background: var(--page-bg);
  }
  .canvas {
    position: relative;
    width: 1200px;
    height: 800px;
  }
  .business-card {
    position: absolute;
    left: 271px;
    top: 201px;
    width: 660px;
    height: 403px;
    overflow: hidden;
    background: linear-gradient(180deg, var(--card-light) 35%, var(--card-shade) 100%);
  }
  .card-art {
    position: absolute;
    inset: 0;
    width: 660px;
    height: 403px;
  }
  .brand {
    position: absolute;
    left: 40px;
    top: 62px;
    display: flex;
    align-items: center;
    gap: 12px;
  }
  .brand-dot {
    width: 22px;
    height: 22px;
    border-radius: 50%;
    background: #ffffff;
  }
  .brand-name {
    font-family: "Questrial", sans-serif;
    font-size: 34px;
    color: #ffffff;
    letter-spacing: 1px;
    line-height: 1;
  }
  .identity {
    position: absolute;
    left: 0;
    width: 100%;
    top: 179px;
    text-align: center;
    font-family: "Questrial", sans-serif;
    font-size: 29px;
    line-height: 1.2;
    white-space: nowrap;
  }
  .person-name { color: var(--name-blue); }
  .divider {
    display: inline-block;
    width: 1px;
    height: 26px;
    background: var(--rule-grey);
    margin: 0 10px;
    vertical-align: -3px;
  }
  .person-title { color: var(--title-ink); }
  .contact-list {
    position: absolute;
    left: 0;
    width: 100%;
    top: 226px;
    text-align: center;
    font-family: "Open Sans", sans-serif;
    font-size: 16.5px;
    line-height: 23px;
    color: var(--body-ink);
    list-style: none;
  }
  .office-address {
    position: absolute;
    left: 0;
    width: 100%;
    top: 352px;
    text-align: center;
    font-family: "Open Sans", sans-serif;
    font-size: 16.5px;
    color: var(--body-ink);
    font-style: normal;
  }
</style>
</head>
<body>
<main class="canvas">
  <section class="business-card">
    <svg class="card-art" viewBox="0 0 660 403" aria-hidden="true">
      <defs>
        <linearGradient id="bandFill" x1="0" y1="0" x2="1" y2="1">
          <stop offset="0" stop-color="#1a76a3"/>
          <stop offset="0.6" stop-color="#17709c"/>
          <stop offset="1" stop-color="#0f5d86"/>
        </linearGradient>
      </defs>
      <path d="M0,0 H660 V100 C470,130 250,166 0,164 Z" fill="var(--rule-grey)"/>
      <path d="M0,0 H660 V94 C470,124 250,160 0,158 Z" fill="url(#bandFill)"/>
      <path d="M60,0 C120,70 260,120 420,104 C530,92 610,60 660,28 V0 Z" fill="var(--brand-blue-light)" opacity="0.25"/>
      <path d="M300,0 C380,30 520,40 660,10 V0 Z" fill="var(--brand-blue-deep)" opacity="0.35"/>
      <path d="M260,403 C380,360 520,320 660,230 V403 Z" fill="#ffffff" opacity="0.45"/>
      <path d="M0,330 C180,300 420,310 660,250 V403 H0 Z" fill="#d9dadc" opacity="0.35"/>
    </svg>

    <div class="brand">
      <span class="brand-dot"></span>
      <span class="brand-name">LORM</span>
    </div>

    <h1 class="identity">
      <span class="person-name">Rafiqul Haque</span><span class="divider"></span><span class="person-title">Co Founder</span>
    </h1>

    <ul class="contact-list">
      <li>ph: 14320 517 2908 &nbsp;|&nbsp; mob: &nbsp;052 614 3390</li>
      <li>email: rhaque07@mailnest.com</li>
      <li>www.lormpgh.com</li>
    </ul>

    <address class="office-address">718, Saffron Crest Tower, Palmwood Garden Heights, Dubai, U.A.E</address>
  </section>
</main>
</body>
</html>
```